Business card design needed-Cake Decorating

I personalize designer cakes without the designer price. I was thinking about a card design that is a little funky, modern and fun. I am very open to suggestions though

Industry/Entity Type

Business

Contact Information for Business Card

Whisk & Bloom Bakehouse
Ph: Mara Pelling 0438105274
Email:mara@whiskbloombakehouse.com.au
Website:www.whiskbloombakehouse.com.au
ABN: 47 293816054

```html
<!DOCTYPE html>
<html lang="en">
<head>
<meta charset="utf-8">
<title>Whisk &amp; Bloom Bakehouse – Business Card</title>
<link rel="stylesheet" href="https://fonts.googleapis.com/css2?family=Fredoka:wght@500;600&display=swap">
<style>
  :root {
    --card-bg: #dcdddd;
    --card-border: #3a3a3a;
    --brand-purple: #3b3287;
    --ink: #2f2f2f;
    --cake-pink: #e6127f;
    --cake-light-pink: #f08cc4;
    --cake-blue: #0ea2df;
    --cake-yellow: #f6ea16;
    --cake-orange: #f5821f;
  }
  * { margin: 0; padding: 0; box-sizing: border-box; }
  html, body { width: 1200px; height: 677px; overflow: hidden; background: var(--card-bg); }
  .card {
    position: relative;
    width: 1200px;
    height: 677px;
    background: var(--card-bg);
    border: 2px solid var(--card-border);
    font-family: "Fredoka", sans-serif;
    overflow: hidden;
  }
  .cake-art {
    position: absolute;
    left: 712px;
    top: 66px;
    width: 430px;
    height: 348px;
  }
  .brand-name {
    position: absolute;
    left: 84px;
    top: 72px;
    color: var(--brand-purple);
    font-weight: 600;
    line-height: 1;
  }
  .brand-name .line-main { display: block; font-size: 132px; letter-spacing: 1px; }
  .brand-name .line-sub { display: block; font-size: 100px; margin-top: 30px; letter-spacing: 2px; }
  .contact-list {
    position: absolute;
    left: 56px;
    top: 456px;
    list-style: none;
    color: var(--ink);
    font-weight: 500;
    font-size: 33px;
  }
  .contact-item {
    display: flex;
    align-items: center;
    height: 61px;
  }
  .contact-icon {
    width: 46px;
    height: 42px;
    margin-right: 20px;
    flex: none;
  }
  .social-square {
    width: 40px;
    height: 40px;
    margin: 0 26px 0 3px;
    background: var(--ink);
    flex: none;
  }
  .abn {
    position: absolute;
    left: 741px;
    top: 521px;
    color: var(--ink);
    font-weight: 500;
    font-size: 36px;
  }
</style>
</head>
<body>
<div class="card">
  <svg class="cake-art" viewBox="0 0 430 348" role="img" aria-label="Illustration of a two-tier pink and blue cake with yellow and orange drip icing">
    <defs>
      <linearGradient id="cakeTone" x1="0" y1="0" x2="0" y2="1">
        <stop offset="0" stop-color="var(--cake-light-pink)"/>
        <stop offset="0.4" stop-color="var(--cake-pink)"/>
        <stop offset="0.55" stop-color="var(--cake-blue)"/>
        <stop offset="0.7" stop-color="var(--cake-orange)"/>
        <stop offset="0.85" stop-color="var(--cake-pink)"/>
        <stop offset="1" stop-color="var(--cake-pink)"/>
      </linearGradient>
    </defs>
    <rect x="0" y="0" width="430" height="348" rx="60" fill="url(#cakeTone)"/>
  </svg>

  <h1 class="brand-name">
    <span class="line-main">Whisk &amp; Bloom</span>
    <span class="line-sub">Bakehouse</span>
  </h1>

  <ul class="contact-list">
    <li class="contact-item">
      <svg class="contact-icon" viewBox="0 0 46 42" aria-hidden="true">
        <path d="M4 12 Q23 0 42 12 L42 17 L34 17 L34 12 Q23 8 12 12 L12 17 L4 17 Z" fill="var(--ink)"/>
        <path d="M10 18 L36 18 L42 40 L4 40 Z" fill="var(--ink)"/>
        <g fill="var(--card-bg)">
          <rect x="15" y="24" width="4" height="3"/><rect x="21" y="24" width="4" height="3"/><rect x="27" y="24" width="4" height="3"/>
          <rect x="14" y="30" width="4" height="3"/><rect x="21" y="30" width="4" height="3"/><rect x="28" y="30" width="4" height="3"/>
        </g>
      </svg>
      <span>0438105274 (Mara Pelling)</span>
    </li>
    <li class="contact-item">
      <svg class="contact-icon" viewBox="0 0 46 42" aria-hidden="true">
        <rect x="3" y="8" width="40" height="28" fill="none" stroke="var(--ink)" stroke-width="3"/>
        <path d="M3 8 L23 25 L43 8 M3 36 L18 21 M43 36 L28 21" fill="none" stroke="var(--ink)" stroke-width="3"/>
      </svg>
      <span>mara@whiskbloombakehouse.com.au</span>
    </li>
    <li class="contact-item">
      <span class="social-square" aria-hidden="true"></span>
      <span>Whisk &amp; Bloom Bakehouse</span>
    </li>
  </ul>

  <p class="abn">ABN: 47 293816054</p>
</div>
</body>
</html>
```